Cover for CD-single

TOVA is a young singer-songwriter and needs a CD cover design for her first single "Stars over harbour". Her song is about her best friend who recently moved from Europe to Australia with her family. But even though they now live on the other side of the world, they will always be there for each other.
You can use the picture attached or you can see it as an inspiration.
Please put the name of the artist: TOVA
and the name of the song on the cover: Stars over harbour

```html
<!DOCTYPE html>
<html lang="en">
<head>
<meta charset="utf-8">
<title>TOVA – Stars over harbour</title>
<link rel="stylesheet" href="https://fonts.googleapis.com/css2?family=Raleway:wght@300&family=Cookie&display=swap">
<style>
  :root {
    --sky-top: #4a4fb0;
    --sky-mid: #9a7ad6;
    --horizon: #f0a8d8;
    --mountain: #b7a3e6;
    --ridge: #4f58b8;
    --water: #7aa6f0;
    --water-glow: #e9b6ec;
    --city: #4a4aa6;
    --hill-dark: #2f3486;
    --bench-glow: #f07ee6;
    --meadow: #c56adf;
    --meadow-left: #e99ad8;
    --meadow-deep: #2e1a66;
    --text-white: #ffffff;
  }
  * { margin: 0; padding: 0; box-sizing: border-box; }
  html, body {
    width: 1200px;
    height: 1200px;
    overflow: hidden;
    background: var(--meadow-deep);
  }
  .cover {
    position: relative;
    width: 1200px;
    height: 1200px;
    overflow: hidden;
  }
  .cover-artwork {
    position: absolute;
    inset: 0;
    background:
      radial-gradient(ellipse 26% 22% at 54% 70%, rgba(255, 150, 240, 0.75), transparent 72%),
      radial-gradient(ellipse 32% 18% at 54% 84%, rgba(240, 110, 230, 0.6), transparent 75%),
      radial-gradient(ellipse 22% 26% at 8% 80%, rgba(240, 160, 215, 0.65), transparent 75%),
      radial-gradient(ellipse 30% 14% at 90% 38%, rgba(40, 44, 120, 0.7), transparent 75%),
      radial-gradient(ellipse 40% 8% at 48% 38%, rgba(233, 182, 236, 0.6), transparent 75%),
      radial-gradient(ellipse 30% 7% at 80% 47%, rgba(150, 200, 255, 0.55), transparent 75%),
      radial-gradient(ellipse 35% 10% at 75% 18%, rgba(255, 170, 220, 0.6), transparent 75%),
      radial-gradient(ellipse 45% 18% at 50% 100%, rgba(40, 20, 100, 0.8), transparent 75%),
      linear-gradient(180deg,
        var(--sky-top) 0%,
        var(--sky-mid) 9%,
        var(--horizon) 18%,
        var(--mountain) 24%,
        var(--ridge) 30%,
        var(--water-glow) 35%,
        var(--water) 41%,
        var(--city) 48%,
        var(--water) 55%,
        var(--city) 62%,
        var(--meadow) 76%,
        var(--meadow-deep) 100%);
  }
  .artist-name {
    position: absolute;
    left: 184px;
    top: 118px;
    width: 812px;
    display: flex;
    justify-content: space-between;
    font-family: "Raleway", sans-serif;
    font-weight: 300;
    font-size: 188px;
    line-height: 1;
    color: var(--text-white);
    text-shadow: 0 2px 10px rgba(60, 30, 120, 0.3);
  }
  .song-title {
    position: absolute;
    left: 160px;
    width: 860px;
    top: 1012px;
    text-align: center;
    font-family: "Cookie", cursive;
    font-weight: 400;
    font-size: 128px;
    line-height: 1;
    white-space: nowrap;
    color: var(--text-white);
    text-shadow: 0 3px 10px rgba(40, 10, 90, 0.45);
  }
</style>
</head>
<body>
  <main class="cover">
    <div class="cover-artwork" role="img" aria-label="Illustration: two best friends hugging on a wooden bench on a flowery hillside at dusk, looking out over a glowing harbour city and lake towards snowy pink mountains under a purple evening sky"></div>
    <h1 class="artist-name" aria-label="TOVA">
      <span>T</span><span>O</span><span>V</span><span>A</span>
    </h1>
    <h2 class="song-title">Stars over harbour</h2>
  </main>
</body>
</html>
```